Business and Success Coaching Business Card

Need a business card for my coaching business. I coach small businesses, career professionals and, individuals wanting to unlock their human potential and achieve excellence. At the heart of our methodology is the Shaping Purposeful Action Routines Knowingly (SPARK) approach to formulate empowerment, create principles for success and setting achievable outcomes. I would like something that incorporates our new logo, something clean and sharp with a solid darker, but complementary background, color on the card front. The back should be white where there will be room for three questions

Target Market(s)

People looking to advance and improve themselves through a success coach

Industry/Entity Type

Life Coaching

Contact Information for Business Card

Contact information on card.
Business name on front of card
Questions on back

Font styles to use
Other font styles liked:
• Century Gothic or other Serif style fonts that look similar to Century Gothic

Colors

Designer to choose colors to be used in the design.

Requirements
Must have
• Logo on front of card
• Business name - The Steady Forge
• Contact name - Ted Harlow
• Address - Box 4619, Alder Falls, OR 97491-4619
• Phone number - 303-555-0147
• Email address - harlow.ted@thesteadyforge.example
• Certifications - CPC, ACC, MBA
• Back of card
• Three questions on the back of the card:
• If you were at your best, what would you do right now?
• What is the decision you have been avoiding?
• What's one action you could take in the next 10 minutes?
Nice to have
• I would like to see a solid color on the front of the card that compliments the logo.
• Back should be white, or could be contrasting, but need to have the three questions.

```html
<!DOCTYPE html>
<html lang="en">
<head>
<meta charset="utf-8">
<title>The Steady Forge – Business Card</title>
<link href="https://fonts.googleapis.com/css2?family=Lato:wght@400;700&display=swap" rel="stylesheet">
<style>
  :root {
    --navy: #253f8e;
    --navy-deep: #1f3880;
    --navy-light: #4466b0;
    --sky: #7bb6df;
    --sky-text: #8cc0ea;
    --white: #ffffff;
    --paper: #f6f6f7;
    --stage: #e9e9ec;
  }
  * { box-sizing: border-box; margin: 0; padding: 0; }
  html, body {
    width: 789px; height: 1200px; overflow: hidden;
    background: var(--stage);
    font-family: "Lato", sans-serif;
  }
  .canvas {
    width: 789px; height: 1200px;
    display: flex; flex-direction: column; align-items: center; justify-content: center;
    gap: 80px;
  }
  .card {
    position: relative;
    width: 700px; height: 400px;
    border-radius: 16px;
    overflow: hidden;
    box-shadow: 0 6px 18px rgba(0,0,0,.18);
  }

  /* Contact side */
  .card--contact { background: linear-gradient(135deg, var(--white), var(--paper)); }
  .card--contact .panel { position: absolute; inset: 0; width: 100%; height: 100%; }
  .brand {
    position: absolute; left: 48px; top: 160px;
    display: flex; align-items: center; gap: 12px;
  }
  .brand__dot { width: 18px; height: 18px; border-radius: 50%; background: var(--navy); }
  .brand__name { font-weight: 700; font-size: 34px; color: var(--navy); white-space: nowrap; }
  .brand__tagline {
    position: absolute; left: 78px; top: 206px;
    font-size: 17px; color: var(--sky);
  }
  .contact {
    position: absolute; right: 40px; top: 62px;
    text-align: right; color: var(--white);
  }
  .contact__name {
    font-weight: 700; font-size: 30px; letter-spacing: 2px;
    color: var(--sky-text); text-transform: uppercase;
  }
  .contact__certs { font-size: 17px; margin-top: 4px; }
  .contact__address { font-size: 17px; margin-top: 18px; line-height: 1.35; }
  .contact__lines { margin-top: 22px; font-size: 16px; line-height: 1.75; }
  .contact__line { display: flex; justify-content: flex-end; align-items: center; gap: 8px; white-space: nowrap; }
  .icon { width: 13px; height: 13px; fill: none; stroke: var(--sky-text); stroke-width: 1.6; }

  /* Questions side */
  .card--questions {
    background: linear-gradient(160deg, var(--navy-deep) 0%, var(--navy) 45%, var(--navy-light) 100%);
    color: var(--white); text-align: center;
  }
  .questions__brand {
    position: absolute; left: 0; right: 0; top: 92px;
    display: flex; justify-content: center; align-items: center; gap: 14px;
  }
  .questions__brand .brand__dot { background: var(--white); width: 20px; height: 20px; }
  .questions__brand .brand__name { color: var(--white); font-size: 44px; }
  .questions__tagline { position: absolute; left: 0; right: 0; top: 152px; font-size: 22px; }
  .questions__list {
    position: absolute; left: 0; right: 0; top: 222px;
    list-style: none; font-size: 19px; line-height: 1.65;
  }
</style>
</head>
<body>
<main class="canvas">

  <section class="card card--contact" aria-label="Card side with contact details">
    <svg class="panel" viewBox="0 0 700 400" preserveAspectRatio="none" aria-hidden="true">
      <path d="M420 0 Q330 200 372 400 L700 400 L700 0 Z" fill="var(--sky)"/>
      <path d="M436 0 Q348 200 390 400 L700 400 L700 0 Z" fill="var(--navy)"/>
    </svg>
    <div class="brand">
      <span class="brand__dot"></span>
      <span class="brand__name">The Steady Forge</span>
    </div>
    <p class="brand__tagline">Build your next chapter</p>
    <div class="contact">
      <p class="contact__name">Ted Harlow</p>
      <p class="contact__certs">CPC, ACC, MBA</p>
      <p class="contact__address">Box 4619, Alder Falls,<br>OR 97491-4619</p>
      <div class="contact__lines">
        <p class="contact__line">303-555-0147
          <svg class="icon" viewBox="0 0 14 14"><path d="M3 1 L5 4 L4 6 Q6 9 8 10 L10 9 L13 11 L11 13 Q4 12 1 3 Z"/></svg></p>
        <p class="contact__line">harlow.ted@thesteadyforge.example
          <svg class="icon" viewBox="0 0 14 14"><rect x="1" y="3" width="12" height="8"/><path d="M1 3 L7 8 L13 3"/></svg></p>
        <p class="contact__line">www.thesteadyforge.example
          <svg class="icon" viewBox="0 0 14 14"><circle cx="7" cy="7" r="6"/><path d="M1 7 H13 M7 1 Q3 7 7 13 Q11 7 7 1"/></svg></p>
      </div>
    </div>
  </section>

  <section class="card card--questions" aria-label="Card side with coaching questions">
    <div class="questions__brand">
      <span class="brand__dot"></span>
      <span class="brand__name">The Steady Forge</span>
    </div>
    <p class="questions__tagline">Build your next chapter</p>
    <ul class="questions__list">
      <li>If you were at your best, what would you do right now?</li>
      <li>What is the decision you have been avoiding?</li>
      <li>What's one action you could take in the next 10 minutes?</li>
    </ul>
  </section>

</main>
</body>
</html>
```